Looking for a high-end business card design for a construction company

We are looking to update our business card design. We are a post-frame construction company that builds custom buildings, commercial spaces, homes, and anything else. We have multiple people working here so we would need something we can easily customize the information for the specific person. We need a name, website, cell phone, office phone as well as social icons. Our colors are black, white, and grey/silver so I would love a black background or something that is more striking than just a traditional white business card. Looking for something that is very professional with a high-end look/feel. I have attached our logos, they can be silver, white, grey, or black.
Industry/Entity Type
Construction
Contact Information for Business Card
Business logo, Name, Cell phone, Office phone, website, social Icons
Colors
Designer to choose only greyscale colors for use in the design.
Look and feel

```html
<!DOCTYPE html>
<html lang="en">
<head>
<meta charset="utf-8">
<title>Harlow Frame Works – Business Card</title>
<link rel="stylesheet" href="https://fonts.googleapis.com/css2?family=Montserrat:wght@400;500;700;800&display=swap">
<style>
  :root {
    --stage: #161616;
    --card-front: #1e1e1e;
    --card-back: #0c0c0c;
    --pattern-dark: #101010;
    --pattern-light: #2e2e2e;
    --ink: #ffffff;
    --ink-soft: #d9d9d9;
    --edge: #2a2a2a;
  }
  * { margin: 0; padding: 0; box-sizing: border-box; }
  html, body {
    width: 1200px; height: 988px; overflow: hidden;
    background: var(--stage);
    font-family: "Montserrat", sans-serif;
  }
  .canvas { position: relative; width: 1200px; height: 988px; }

  .card {
    position: absolute;
    width: 560px; height: 320px;
    border-radius: 22px;
    overflow: hidden;
    box-shadow: 0 18px 40px rgba(0,0,0,.55);
    border: 1px solid var(--edge);
  }

  /* back side */
  .card-back { left: 70px; top: 110px; background: var(--card-back); }
  .card-back .pattern {
    position: absolute; inset: 0;
    background: linear-gradient(135deg, var(--pattern-dark) 0%, var(--pattern-light) 55%, var(--pattern-dark) 100%);
  }
  .card-back .corner-mark {
    position: absolute; right: 30px; bottom: 26px;
    color: var(--ink); font-weight: 800; font-size: 15px; letter-spacing: 2px;
  }

  /* front side */
  .card-front { left: 570px; top: 540px; background: var(--card-front); }
  .brand {
    position: absolute; right: 44px; top: 58px;
    text-align: right; color: var(--ink);
  }
  .brand-name { font-weight: 800; font-size: 42px; letter-spacing: 3px; line-height: 1; }
  .brand-sub { font-weight: 800; font-size: 17px; letter-spacing: 3px; margin-top: 6px; }

  .person { position: absolute; left: 44px; top: 150px; color: var(--ink); }
  .person-name { font-weight: 700; font-size: 22px; letter-spacing: .5px; }
  .person-title { font-weight: 400; font-size: 13px; color: var(--ink-soft); margin-top: 2px; }

  .contact { position: absolute; left: 44px; top: 212px; list-style: none; }
  .contact li {
    display: flex; align-items: center; gap: 9px;
    color: var(--ink); font-size: 13.5px; line-height: 22px;
  }
  .contact svg { width: 13px; height: 13px; flex: none; fill: var(--ink); }
</style>
</head>
<body>
<main class="canvas">

  <section class="card card-back" aria-label="Card back">
    <div class="pattern" role="img" aria-label="Repeating glossy monogram pattern across the card"></div>
    <span class="corner-mark">HARLOW</span>
  </section>

  <section class="card card-front" aria-label="Card front">
    <div class="brand">
      <div class="brand-name">HARLOW</div>
      <div class="brand-sub">FRAME WORKS</div>
    </div>

    <div class="person">
      <div class="person-name">DANA WHITFIELD</div>
      <div class="person-title">Managing Director</div>
    </div>

    <ul class="contact">
      <li>
        <svg viewBox="0 0 24 24" aria-hidden="true"><path d="M6.6 10.8a15.1 15.1 0 0 0 6.6 6.6l2.2-2.2a1 1 0 0 1 1-.25 11.4 11.4 0 0 0 3.6.57 1 1 0 0 1 1 1V20a1 1 0 0 1-1 1A17 17 0 0 1 3 4a1 1 0 0 1 1-1h3.5a1 1 0 0 1 1 1c0 1.25.2 2.45.57 3.57a1 1 0 0 1-.25 1z"/></svg>
        800-555-0142
      </li>
      <li>
        <svg viewBox="0 0 24 24" aria-hidden="true"><path d="M7 1h10a2 2 0 0 1 2 2v18a2 2 0 0 1-2 2H7a2 2 0 0 1-2-2V3a2 2 0 0 1 2-2zm0 3v14h10V4zm5 15.2a1.2 1.2 0 1 0 0 2.4 1.2 1.2 0 0 0 0-2.4z"/></svg>
        248-555-0187
      </li>
      <li>
        <svg viewBox="0 0 24 24" aria-hidden="true"><path d="M2 5h20v14H2zm2 2v.5l8 5.5 8-5.5V7zm0 2.9V17h16V9.9l-8 5.5z"/></svg>
        info@harlowframeworks.com
      </li>
      <li>
        <svg viewBox="0 0 24 24" aria-hidden="true"><path d="M12 2a10 10 0 1 0 0 20 10 10 0 0 0 0-20zm6.9 6h-3a15.6 15.6 0 0 0-1.4-4A8 8 0 0 1 18.9 8zM12 4c.8 1.2 1.5 2.5 1.9 4h-3.8c.4-1.5 1.1-2.8 1.9-4zM4.3 14a8 8 0 0 1 0-4h3.4a16 16 0 0 0 0 4zm.8 2h3a15.6 15.6 0 0 0 1.4 4A8 8 0 0 1 5.1 16zm3-8h-3a8 8 0 0 1 4.4-4 15.6 15.6 0 0 0-1.4 4zM12 20c-.8-1.2-1.5-2.5-1.9-4h3.8c-.4 1.5-1.1 2.8-1.9 4zm2.3-6H9.7a14.6 14.6 0 0 1 0-4h4.6a14.6 14.6 0 0 1 0 4zm.2 6a15.6 15.6 0 0 0 1.4-4h3a8 8 0 0 1-4.4 4zm1.8-6a16 16 0 0 0 0-4h3.4a8 8 0 0 1 0 4z"/></svg>
        www.harlowframeworks.com
      </li>
    </ul>
  </section>

</main>
</body>
</html>
```